Design for Wordpress Theme for site like quillforge.de

Need a new professional Website design, for my wordpress theme
this theme: http://demobay.pexlorn.com/?theme=project
this should be like:
http://www.tul-brosk.de/
http://www.fennwirk.de/
http://www.taskvelm.com/
http://www.dienstkoral.de/
or something new modern design.
The design must be integrated in the wordpress theme .
The language of the site is in german, but the script/theme is multilingual and this should be stay.
The name of my site is bavlorn
The url of my site is bavlorn.de
Note please , it is about 8 pages to design, not only the Startpage
i.e.
- login Page
- User Menu page
- search page
- Project post page
Industry/Entity Type
It Professional
Number of Pages Required
5+ page
Look and feel
Each slider illustrates characteristics of the customer's brand and the style your logo design should communicate.

```html
<!DOCTYPE html>
<html lang="en">
<head>
<meta charset="utf-8">
<title>PlanCrest – Find Local Freelancers</title>
<link href="https://fonts.googleapis.com/css2?family=Raleway:wght@400;500;600;700&family=Open+Sans:wght@400;600;700&display=swap" rel="stylesheet">
<style>
:root{
  --navy:#232b5a;
  --navy-deep:#0f1535;
  --navy-bottom:#0a0f2b;
  --blue:#2a9fe0;
  --blue-title:#2a8fd6;
  --orange:#f47a20;
  --gold:#d07a12;
  --green:#6a9a1f;
  --grey-band:#efefef;
  --text:#222;
  --muted:#666;
  --line:#e2e2e2;
  --white:#fff;
}
*{box-sizing:border-box;margin:0;padding:0}
html,body{width:1200px;height:2671px;overflow:hidden}
body{font-family:"Open Sans",Arial,sans-serif;color:var(--text);background:var(--white)}
a{color:inherit;text-decoration:none}
.container{width:920px;margin-left:140px;position:relative}
h2,h3,.brand{font-family:"Raleway",Arial,sans-serif}

/* header */
.site-header{height:85px;background:var(--navy);display:flex;align-items:center}
.site-header .container{display:flex;align-items:center;justify-content:space-between;width:920px}
.brand{display:flex;align-items:center;gap:10px;color:var(--white);font-size:24px;font-weight:700}
.brand-mark{width:30px;height:30px;background:var(--orange);border-radius:4px}
.main-nav{display:flex;font-size:15px;color:var(--white)}
.main-nav a{padding:0 20px;border-left:1px solid rgba(255,255,255,.3)}
.main-nav a:first-child{border-left:none}
.main-nav a:last-child{padding-right:0}

/* hero */
.hero{height:428px;position:relative;background:linear-gradient(110deg,#e9e4dc 0%,#d8cfc0 45%,#8a6a4e 75%,#5a4a3e 100%)}
.hero-card{position:absolute;left:142px;top:65px;width:322px;height:273px;background:var(--blue);border-radius:3px;padding:30px 25px;color:var(--white)}
.hero-card h1{font-family:"Raleway",sans-serif;font-size:24px;font-weight:600;line-height:1.15;white-space:nowrap}
.hero-card h1 span{display:block;font-size:20px;margin-top:2px}
.hero-card p{font-size:11px;line-height:1.5;margin-top:10px;opacity:.9}
.search-box{margin-top:14px;height:34px;background:var(--white);border-radius:2px;display:flex;align-items:center;justify-content:space-between;padding:0 12px;color:#555;font-size:11px}
.hero-actions{display:flex;gap:6px;margin-top:10px}
.btn{height:38px;display:flex;align-items:center;justify-content:center;font-size:12px;color:var(--white);border-radius:2px}
.btn-dark{width:136px;background:var(--navy-deep)}
.btn-green{width:132px;background:var(--green)}

/* categories */
.categories{height:299px;text-align:center;position:relative}
.section-title{font-size:26px;font-weight:500;color:#222}
.categories .section-title{padding-top:44px}
.cat-list{display:flex;justify-content:space-between;margin-top:40px}
.cat-item{width:225px}
.cat-item svg{display:block;margin:0 auto}
.cat-item h3{font-size:21px;font-weight:500;margin-top:8px}
.cat-item p{font-size:10px;color:var(--muted);line-height:1.5;margin-top:6px}
.slide-arrow{position:absolute;top:150px}
.slide-arrow.prev{left:104px}
.slide-arrow.next{right:104px}

/* featured */
.featured{height:376px;background:var(--grey-band);border-top:1px solid var(--line)}
.featured-head{display:flex;justify-content:space-between;align-items:center;padding-top:48px}
.featured-head .section-title{font-size:27px}
.cards{display:flex;gap:12px;margin-top:18px}
.card{width:221px;height:222px;background:var(--white);border:1px solid #d8d8d8;border-radius:3px;overflow:hidden}
.card-photo{height:138px}
.card-body{padding:16px 24px;font-size:15px;color:var(--navy)}
.price{color:var(--gold);display:block;margin-top:4px;font-size:16px}

/* latest */
.latest{height:427px}
.latest .section-title{color:var(--blue-title);font-size:27px;padding-top:52px}
.project-grid{display:grid;grid-template-columns:469px 451px;row-gap:42px;margin-top:22px}
.project{display:flex;gap:14px}
.project-photo{width:124px;height:98px;flex:none}
.project h3{font-size:15px;font-weight:500;color:var(--navy)}
.project p{font-size:10px;color:var(--muted);line-height:1.6;margin-top:4px;width:310px}
.meta{font-size:10.5px;color:var(--text);margin-top:6px;line-height:1.9}

/* locations */
.locations{height:343px;background:var(--orange);color:var(--white)}
.locations .section-title{color:var(--white);font-size:29px;padding-top:46px}
.loc-grid{display:flex;justify-content:space-between;margin-top:18px;width:925px}
.loc-col h3{font-size:14px;font-weight:500;margin-bottom:10px}
.loc-col li{list-style:none;font-size:10.5px;line-height:29px;font-weight:600}

/* most viewed */
.most-viewed{height:394px}
.most-viewed .container{display:flex;justify-content:space-between}
.mv-main{width:660px}
.most-viewed .section-title{font-size:22px;padding-top:50px}
.mv-grid{display:grid;grid-template-columns:330px 330px;row-gap:32px;margin-top:24px}
.mv-item{display:flex;gap:14px}
.mv-photo{width:124px;height:90px;flex:none}
.mv-item h3{font-size:15px;font-weight:500;color:var(--navy)}
.mv-item p{font-size:10px;color:var(--muted);line-height:1.6;margin-top:2px;width:185px}
.mv-item p + p{margin-top:0}
.read-more{font-size:10px;font-weight:700;color:#2a6fb0;margin-top:2px;display:block}
.social-box{width:235px;height:285px;border:1px solid #d5d5d5;margin-top:57px;padding:18px 20px;font-size:10px;color:#444}
.sb-head{display:flex;gap:10px}
.sb-logo{width:46px;height:44px;background:#3b5aa8;border:1px solid #ccc}
.sb-head strong{font-size:12px;display:block}
.sb-like{display:inline-block;margin-top:4px;border:1px solid #aab;padding:1px 6px;font-size:9px}
.sb-count{margin-top:12px}
.faces{display:grid;grid-template-columns:repeat(4,44px);gap:5px;margin-top:8px}
.faces div{height:44px;background:linear-gradient(135deg,#b79a86,#6a5a56)}
.sb-foot{margin-top:12px;display:flex;align-items:center;gap:6px;font-size:9px}
.sb-foot i{width:10px;height:10px;background:#3b5aa8;display:block}

/* footer */
.site-footer{height:251px;background:var(--navy-deep);color:var(--white)}
.footer-cols{display:flex;padding-top:58px}
.f-col h3{font-size:15px;font-weight:600;letter-spacing:.5px;margin-bottom:10px}
.f-col li{list-style:none;font-size:12px;line-height:25px}
.f-info{width:205px;height:152px;border-right:1px solid rgba(255,255,255,.2)}
.f-cats{width:380px;padding-left:55px;height:152px;border-right:1px solid rgba(255,255,255,.2)}
.f-cats .sub{display:flex;gap:86px}
.f-res{padding-left:72px}
.bottom-bar{height:68px;background:var(--navy-bottom);color:#9aa0b8}
.bottom-bar .container{display:flex;justify-content:space-between;align-items:center;height:68px;font-size:10.5px}
.social{display:flex;gap:5px}
.social span{width:22px;height:22px;background:var(--white);border-radius:3px;display:block}
</style>
</head>
<body>

<header class="site-header">
  <div class="container">
    <a class="brand" href="#"><span class="brand-mark"></span>PlanCrest</a>
    <nav class="main-nav">
      <a href="#">WP-Admin</a><a href="#">Post New</a><a href="#">Blog</a><a href="#">My Account</a><a href="#">Logout</a>
    </nav>
  </div>
</header>

<section class="hero" role="img" aria-label="Photo of a smiling craftsman cutting wood with a circular saw">
  <div class="hero-card">
    <h1>Find Local Freelancers<span>Get your project done.</span></h1>
    <p>Mauris vel lacus vitae felis vestibulum volutpat Etiam est nunc venenatis in tristique</p>
    <div class="search-box">Type Service
      <svg width="14" height="14" viewBox="0 0 14 14"><circle cx="6" cy="6" r="4.5" fill="none" stroke="#666" stroke-width="1.5"/><path d="M9.5 9.5l3.5 3.5" stroke="#666" stroke-width="1.5"/></svg>
    </div>
    <div class="hero-actions">
      <a class="btn btn-dark" href="#">Post Your Project</a>
      <a class="btn btn-green" href="#">Join Us It's Free</a>
    </div>
  </div>
</section>

<section class="categories">
  <h2 class="section-title">Browse Freelancer Categories</h2>
  <svg class="slide-arrow prev" width="20" height="42" viewBox="0 0 20 42"><path d="M18 2L3 21l15 19" fill="none" stroke="#999" stroke-width="1.5"/></svg>
  <svg class="slide-arrow next" width="20" height="42" viewBox="0 0 20 42"><path d="M2 2l15 19L2 40" fill="none" stroke="#999" stroke-width="1.5"/></svg>
  <div class="container cat-list">
    <div class="cat-item">
      <svg width="40" height="36" viewBox="0 0 40 36"><rect x="2" y="2" width="36" height="24" rx="2" fill="none" stroke="#2a9fe0" stroke-width="3"/><rect x="16" y="26" width="8" height="5" fill="#2a9fe0"/><rect x="10" y="31" width="20" height="3" fill="#2a9fe0"/></svg>
      <h3>Computers</h3><p>Class aptent taciti sociosqu ad litora torquent per conubia nostra pdeder</p>
    </div>
    <div class="cat-item">
      <svg width="40" height="36" viewBox="0 0 40 36"><rect x="2" y="2" width="36" height="24" rx="2" fill="none" stroke="#2a9fe0" stroke-width="3"/><rect x="16" y="26" width="8" height="5" fill="#2a9fe0"/><rect x="10" y="31" width="20" height="3" fill="#2a9fe0"/></svg>
      <h3>Housework</h3><p>Class aptent taciti sociosqu ad litora torquent per conubia nostra pdeder</p>
    </div>
    <div class="cat-item">
      <svg width="40" height="36" viewBox="0 0 40 36"><rect x="14" y="2" width="12" height="8" rx="2" fill="none" stroke="#2a9fe0" stroke-width="3"/><rect x="2" y="9" width="36" height="25" rx="3" fill="#2a9fe0"/><rect x="2" y="19" width="36" height="2" fill="#fff"/><rect x="17" y="17" width="6" height="6" fill="#fff"/></svg>
      <h3>Office Help</h3><p>Class aptent taciti sociosqu ad litora torquent per conubia nostra pdeder</p>
    </div>
    <div class="cat-item">
      <svg width="44" height="36" viewBox="0 0 44 36"><path d="M13 8L3 18l10 10M31 8l10 10-10 10M25 4l-6 28" fill="none" stroke="#2a9fe0" stroke-width="3.5"/></svg>
      <h3>Programming</h3><p>Class aptent taciti sociosqu ad litora torquent per conubia nostra pdeder</p>
    </div>
  </div>
</section>

<section class="featured">
  <div class="container">
    <div class="featured-head">
      <h2 class="section-title">Featured Projects of the Day</h2>
      <svg width="30" height="16" viewBox="0 0 30 16"><path d="M9 2L3 8l6 6M21 2l6 6-6 6" fill="none" stroke="#555" stroke-width="1.6"/></svg>
    </div>
    <div class="cards">
      <article class="card"><div class="card-photo" role="img" aria-label="Photo of a father and child working on a laptop" style="background:linear-gradient(135deg,#8a5a3a,#3a2a2a)"></div><div class="card-body">Fix my old Nexaphone, 3gs<span class="price">($100 - $500)</span></div></article>
      <article class="card"><div class="card-photo" role="img" aria-label="Photo of a hand repairing an air conditioner" style="background:linear-gradient(135deg,#e8e8e8,#a8a8a8)"></div><div class="card-body">Fix my old Nexaphone, 3gs<span class="price">($100 - $500)</span></div></article>
      <article class="card"><div class="card-photo" role="img" aria-label="Photo of hands fixing a bathroom sink" style="background:linear-gradient(135deg,#b8d8d0,#6aa8a0)"></div><div class="card-body">Fix my old Nexaphone, 3gs<span class="price">($100 - $500)</span></div></article>
      <article class="card"><div class="card-photo" role="img" aria-label="Photo of a man on a ladder outside a house" style="background:linear-gradient(135deg,#7a7a6a,#3a3a3a)"></div><div class="card-body">Fix my old Nexaphone, 3gs<span class="price">($100 - $500)</span></div></article>
    </div>
  </div>
</section>

<section class="latest">
  <div class="container">
    <h2 class="section-title">Latest Projects</h2>
    <div class="project-grid">
      <article class="project"><div class="project-photo" role="img" aria-label="Photo of hands working on a car engine" style="background:linear-gradient(135deg,#5a6a7a,#2a2e34)"></div><div><h3>Fix my car engine</h3><p>Mauris vel lacus vitae felis vestibulum volutpat Etiam est nunc venenatis in tristique eu imperdiet ac nisl Cum sociis</p><div class="meta">Huge Project ($1,200 - $10,000) &nbsp;|&nbsp; 14th May 2013<br>7 days, 14 hours, 1 min &nbsp;|&nbsp; 1 proposals</div></div></article>
      <article class="project"><div class="project-photo" role="img" aria-label="Photo of a repairman fixing a washing machine" style="background:linear-gradient(135deg,#c8b8a8,#7a6a5a)"></div><div><h3>Fix my car engine</h3><p>Mauris vel lacus vitae felis vestibulum volutpat Etiam est nunc venenatis in tristique eu imperdiet ac nisl Cum sociis</p><div class="meta">Huge Project ($1,200 - $10,000) &nbsp;|&nbsp; 14th May 2013<br>7 days, 14 hours, 1 min &nbsp;|&nbsp; 1 proposals</div></div></article>
      <article class="project"><div class="project-photo" role="img" aria-label="Photo of a mechanic under a car" style="background:linear-gradient(135deg,#a89888,#4a5a7a)"></div><div><h3>Fix my car engine</h3><p>Mauris vel lacus vitae felis vestibulum volutpat Etiam est nunc venenatis in tristique eu imperdiet ac nisl Cum sociis</p><div class="meta">Huge Project ($1,200 - $10,000) &nbsp;|&nbsp; 14th May 2013<br>7 days, 14 hours, 1 min &nbsp;|&nbsp; 1 proposals</div></div></article>
      <article class="project"><div class="project-photo" role="img" aria-label="Photo of a technician and a customer beside a refrigerator" style="background:linear-gradient(135deg,#d8d0c8,#8a7a70)"></div><div><h3>Fix Refrigator</h3><p>Mauris vel lacus vitae felis vestibulum volutpat Etiam est nunc venenatis in tristique eu imperdiet ac nisl Cum sociis</p><div class="meta">Huge Project ($1,200 - $10,000) &nbsp;|&nbsp; 14th May 2013<br>7 days, 14 hours, 1 min &nbsp;|&nbsp; 1 proposals</div></div></article>
    </div>
  </div>
</section>

<section class="locations">
  <div class="container">
    <h2 class="section-title">Locations</h2>
    <div class="loc-grid">
      <div class="loc-col"><h3>California(0)</h3><ul><li>Bakersfield (0)</li><li>Los Angeles (0)</li><li>Orange (0)</li><li>San Diego (0)</li><li>San Fancisco (0)</li></ul></div>
      <div class="loc-col"><h3>Florida(2)</h3><ul><li>Cape Coral (1)</li><li>Fort Lauderdale (0)</li><li>Miami (0)</li><li>Orlando (0)</li><li>Palm Bay (0)</li></ul></div>
      <div class="loc-col"><h3>Nevada(1)</h3><ul><li>Carson City (0)</li><li>Henderson (0)</li><li>Las Vegas (0)</li><li>Reno (0)</li><li>Sparks (0)</li></ul></div>
      <div class="loc-col"><h3>New York(3)</h3><ul><li>Bronx (0)</li><li>Long Island (0)</li><li>Manhattan (0)</li><li>New York City (0)</li><li>Queens (0)</li></ul></div>
      <div class="loc-col"><h3>Tennessee(0)</h3><ul><li>Clarksville (0)</li><li>Jackson (0)</li><li>Knoxville (0)</li><li>Memphis (0)</li><li>Nashville (0)</li></ul></div>
      <div class="loc-col"><h3>Texas(1)</h3><ul><li>Amarillo (0)</li><li>Dallas (0)</li><li>El Paso (0)</li><li>Houston (0)</li><li>San Antonio (0)</li></ul></div>
    </div>
  </div>
</section>

<section class="most-viewed">
  <div class="container">
    <div class="mv-main">
      <h2 class="section-title">Most Viewed Projects</h2>
      <div class="mv-grid">
        <article class="mv-item"><div class="mv-photo" role="img" aria-label="Photo of colourful smartphones on a desk" style="background:linear-gradient(135deg,#3a7ab8,#1a2a4a)"></div><div><h3>Fix my car engine</h3><p>Mauris vel lacus vitae felis vestibulum volutpat Etiam est</p><p>Location: Cape Coral, Florida</p><a class="read-more" href="#">READ MORE</a></div></article>
        <article class="mv-item"><div class="mv-photo" role="img" aria-label="Photo of builders in safety vests in a room" style="background:linear-gradient(135deg,#b8a078,#5a4a38)"></div><div><h3>Fix my car engine</h3><p>Mauris vel lacus vitae felis vestibulum volutpat Etiam est</p><p>Location: Cape Coral, Florida</p><a class="read-more" href="#">READ MORE</a></div></article>
        <article class="mv-item"><div class="mv-photo" role="img" aria-label="Photo of a hand holding a smartphone" style="background:linear-gradient(135deg,#a89098,#5a4a5a)"></div><div><h3>Fix my car engine</h3><p>Mauris vel lacus vitae felis vestibulum volutpat Etiam est</p><p>Location: Cape Coral, Florida</p><a class="read-more" href="#">READ MORE</a></div></article>
        <article class="mv-item"><div class="mv-photo" role="img" aria-label="Photo of a couple reviewing plans with a contractor" style="background:linear-gradient(135deg,#d8d8d0,#7a8a9a)"></div><div><h3>Fix my car engine</h3><p>Mauris vel lacus vitae felis vestibulum volutpat Etiam est</p><p>Location: Cape Coral, Florida</p><a class="read-more" href="#">READ MORE</a></div></article>
      </div>
    </div>
    <aside class="social-box">
      <div class="sb-head"><div class="sb-logo"></div><div><strong>pexlorn.com</strong><span class="sb-like">Like</span></div></div>
      <p class="sb-count">1,234 people like pexlorn.com.</p>
      <div class="faces" role="img" aria-label="Grid of member profile photos">
        <div></div><div></div><div></div><div></div><div></div><div></div><div></div><div></div><div></div><div></div><div></div><div></div>
      </div>
      <div class="sb-foot"><i></i>Fanbox social plugin</div>
    </aside>
  </div>
</section>

<footer class="site-footer">
  <div class="container footer-cols">
    <div class="f-col f-info"><h3>INFORMATION</h3><ul><li>About Us</li><li>Contact Us</li><li>Our Terms and Conditions</li><li>Privacy Policy</li></ul></div>
    <div class="f-col f-cats"><h3>CATEGORIES</h3><div class="sub"><ul><li>Computers</li><li>Chores</li><li>Houswork</li><li>Shopping</li></ul><ul><li>Office Help</li><li>Teaching</li><li>Services</li><li>Programming</li></ul></div></div>
    <div class="f-col f-res"><h3>RESOURCES</h3><ul><li>Pexlorn Main Website</li><li>Our Forums</li><li>Another Link</li><li>Yet Another Link</li></ul></div>
  </div>
</footer>
<div class="bottom-bar">
  <div class="container"><span>© 2015 Company Name &nbsp;All right reserved &nbsp;Term of Use</span><div class="social"><span></span><span></span><span></span><span></span></div></div>
</div>

</body>
</html>
```